Broschüre über Mikro-Mobilitätslösungen vom E-Scooter
Zielgruppe
Wir entwickeln und vermarkten Mikro-Mobilitätslösungen vom E-Scooter bis hin zu stationsgebundenen Verleihsystemen. Kunden sind meist Privatleute aber auch Unternehmen, Hotels oder Kommunen. Wir möchten uns und unsere Produkte in einer Broschüre als Story vorstellen und den Leser dazu animieren, sich alles anzusehen. Mit dynamischen QR-Codes soll dann auch auf die Produkte verlinkt werden. Der Text ist nicht final. Möglichst viel davon soll auch optisch dargestelt werden. Dei Anzahl der Seiten der Broschüre spielt zunächt keine Rolle.
Zu jeder Produktvorstellung sollen auchd ie Technischen Daten aufgeführt werden.
Aufgabenstellung
Frisch, einladend, innovativ Broschüre im Format DIN A 5 quer

```html
<!DOCTYPE html>
<html lang="de">
<head>
<meta charset="utf-8">
<title>Wegfalke Broschüre – Seiten 05 und 06</title>
<link href="https://fonts.googleapis.com/css2?family=Bebas+Neue&family=Raleway:wght@300;400;700&display=swap" rel="stylesheet">
<style>
  :root {
    --backdrop: #d8d8d8;
    --paper: #f6f6f6;
    --green: #86b817;
    --green-light: #b3d54a;
    --green-dark: #6aa00c;
    --panel: #eef1e2;
    --ink: #3d3d3d;
    --ink-soft: #555555;
    --rule: #6b6b6b;
  }
  * { margin: 0; padding: 0; box-sizing: border-box; }
  html, body {
    width: 1200px; height: 1089px; overflow: hidden;
    background: var(--backdrop);
  }
  .spread {
    position: absolute; left: 42px; top: 342px;
    width: 1100px; height: 420px;
    display: flex;
    box-shadow: 0 18px 40px rgba(0,0,0,0.18);
  }
  .page {
    position: relative; width: 550px; height: 420px;
    background: var(--paper); overflow: hidden;
  }
  .edge-band {
    position: absolute; top: 0; bottom: 0; left: 0; width: 24px;
    background: linear-gradient(90deg, var(--green-dark), var(--green));
  }
  .side-label {
    position: absolute; top: 140px;
    writing-mode: vertical-rl;
    font-family: "Raleway", sans-serif; font-size: 7px;
    letter-spacing: 2.2px; color: var(--green);
  }
  .tint-panel { position: absolute; background: var(--panel); }
  .kicker {
    position: absolute; font-family: "Bebas Neue", sans-serif;
    font-size: 21px; color: var(--ink); line-height: 1;
  }
  .headline {
    position: absolute; font-family: "Bebas Neue", sans-serif;
    line-height: 1; color: var(--green);
    background: linear-gradient(90deg, var(--green-light), var(--green-dark));
    -webkit-background-clip: text; background-clip: text;
    -webkit-text-fill-color: transparent;
  }
  .dash { position: absolute; height: 6px; width: 36px; background: var(--rule); }
  .body-copy {
    position: absolute; font-family: "Raleway", sans-serif;
    font-size: 8.3px; line-height: 11.2px; color: var(--ink-soft);
  }
  .body-copy p + p { margin-top: 11px; }
  .body-copy strong { font-weight: 700; color: var(--ink); }
  .page-number {
    position: absolute; font-family: "Raleway", sans-serif;
    font-size: 9px; color: var(--ink);
  }
  .spec-badge {
    position: absolute; left: 385px; top: 0; width: 113px; height: 100px;
    border-radius: 0 0 56px 56px;
    background: linear-gradient(90deg, var(--green-light), var(--green));
    padding: 28px 0 0 22px;
    font-family: "Bebas Neue", sans-serif; font-size: 10.5px;
    line-height: 14px; color: #ffffff;
  }
  .left .tint-panel { left: 224px; top: 26px; width: 252px; bottom: 0; }
  .left .side-label { left: 46px; }
  .left .kicker { left: 88px; top: 44px; }
  .left .headline { left: 88px; top: 64px; font-size: 38px; }
  .left .dash { left: 91px; top: 111px; }
  .left .body-copy { left: 87px; top: 128px; width: 330px; }
  .left .page-number { left: 265px; top: 400px; }

  .right .tint-panel { left: 91px; top: 0; width: 271px; height: 308px; }
  .right .side-label { left: 50px; top: 138px; }
  .right .kicker { left: 142px; top: 95px; }
  .right .headline { left: 142px; top: 115px; font-size: 40px; }
  .right .dash { left: 147px; top: 166px; width: 38px; }
  .right .body-copy { left: 142px; top: 184px; width: 348px; }
  .right .page-number { left: 282px; top: 398px; }
</style>
</head>
<body>
  <main class="spread">
    <section class="page left">
      <div class="edge-band"></div>
      <div class="tint-panel"></div>
      <div class="side-label">WEGFALKE One</div>
      <div class="spec-badge">
        Gewicht: 13,5 kg<br>
        Nennleistung: 450 W.<br>
        Reichweite: 29 km
      </div>
      <h2 class="kicker">Die Wegfalke Familie</h2>
      <h1 class="headline">Wegfalke One</h1>
      <div class="dash"></div>
      <div class="body-copy">
        <p>Bringe Dein Fahrerlebnis auf ein neues Level mit dem <strong>WEGFALKE One</strong> – ein Meisterwerk der Leichtigkeit und Wendigkeit. Als Wegbereiter für zukünftige Mobilität begeistert der <strong>WEGFALKE One</strong> mit seinem schlanken Design und seiner agilen Performance, die jeden Moment zu einem besonderen Fahrerlebnis macht.<br>Mit einem Gewicht von nur 13,5 kg begleitet er Dich mühelos durch den urbanen Dschungel. Ob Du ihn die Treppe hinaufträgst oder geschmeidig durch die Straßen lenkst, seine Leichtigkeit macht jeden Weg zum Genuss.</p>
        <p>Der einfache Klappmechanismus eröffnet Dir eine Welt der Freiheit und Unabhängigkeit. Innerhalb von nur 3 Sekunden kannst Du den WEGFALKE One auf- oder zuklappen. Er passt sich nahtlos Deinem Rhythmus an und steht bereit, Dich auf jedes Deiner Abenteuer mitzunehmen.</p>
        <p>Der <strong>WEGFALKE One</strong> stellt sicher, dass Du in guten Händen bist, denn Deine Sicherheit hat oberste Priorität. Mit seinen leistungsstarken und dennoch präzisen dosierbaren Bremsen behältst Du die Kontrolle über jede Situation.</p>
        <p>Der <strong>WEGFALKE One</strong> ist mehr als nur ein Fortbewegungsmittel – er ist Dein treuer Gefährte auf Deinen Reisen. Er verkörpert den Geist der Entdeckung, der Freiheit und der grenzenlosen Freude am Fahren. Spüre den Wind in deinen Haaren, die Energie unter deinen Füßen und die pure Lebensfreude, die der WEGFALKE One Dir schenkt. Erlebe Fahrspaß in seiner reinsten Form - mit dem WEGFALKE One.</p>
      </div>
      <div class="page-number">05</div>
    </section>

    <section class="page right">
      <div class="edge-band"></div>
      <div class="tint-panel"></div>
      <div class="side-label">WEGFALKE One PRO</div>
      <h2 class="kicker">Die Wegfalke Familie</h2>
      <h1 class="headline">Wegfalke One Pro</h1>
      <div class="dash"></div>
      <div class="body-copy">
        <p>Immer noch so leicht und agil, wie Du es gewohnt bist, aber mit mehr Power – das ist die Pro-Version des WEGFALKE One. Ausgestattet mit einem stärkeren Motor und Akku bist Du für jede Herausforderung gerüstet und wirst auf Deinen Fahrten ein neues Level an Fahrvergnügen erleben.</p>
        <p>Freue Dich bei dem neuen Modell außerdem auf leicht bedienbare Blinker an den Lenkerenden, denn Deine Sicherheit im Straßenverkehr hat Vorrang. Deine Sichtbarkeit ist dadurch jederzeit gewährleistet, und Du kannst sorgenfrei und unkompliziert durch die Straßen cruisen. Deine Sicherheit ist unser Antrieb, und diese Innovation trägt dazu bei, dass Du mit ruhigem Gefühl mit Deinem WEGFALKE One Pro unterwegs sein kannst.</p>
        <p>Die Pro-Version des WEGFALKE One bietet Dir ein Fahrerlebnis auf einem neuen Niveau. Leistungsstärker und sicherer als zuvor, eröffnet sie Dir die Möglichkeit, die Straßen mit neuem Schwung zu erkunden. Mach Dich bereit für Abenteuer, Intensität und unvergessliche Momente mit dem WEGFALKE One Pro.</p>
      </div>
      <div class="page-number">06</div>
    </section>
  </main>
</body>
</html>
```